Wedding and event Photography company.

We need a business card design for a photography company based in Singapore named LumaVek. Our core service offering is wedding photojournalism. We would like to see minimalistic designs that use the colour white. The final design should communicate a sense of ease and reliability.

The attached are a couple of visual reference which i found over the web, i hope it will helps.

Project Brief Update (14th July 2014):
- Please refrain from using any images from the website for the design. The laws and regulations over here does not allow me to distribute my client's images. Thanks!

Target Market(s)

Young and middle aged adults aged 24 - 38. With money to spend =D

Industry/Entity Type

Business

Contact Information for Business Card

Name: Dax Pell
Designation: Head Photographer
Mobile: +65 84126079
Email: tan@lumavek.example
Website: www.lumavek.example

Font styles to use
Other font styles liked:
• Baskerville URW

Colors

Designer to choose colors to be used in the design.

Requirements
Must have
• Must include:
• - The brand LumaVek
• - The logo attached
• - Please help to place the brand LumaVek with the logo according to your preferences.
• - Services
• - Wedding Photography
• - Portraiture
• - Photojournalism
Nice to have
• Looking forward to an elegant and simple design. Please see attached examples!
• Please use Serif Fonts
Should not have
• Please refrain from using dark tones for the majority of the design.
• Please refrain from letterpress and embossing.

```html
<!DOCTYPE html>
<html lang="en">
<head>
<meta charset="utf-8">
<title>LumaVek Business Card</title>
<link href="https://fonts.googleapis.com/css2?family=Libre+Baskerville&family=Open+Sans:wght@400;700&display=swap" rel="stylesheet">
<style>
  :root {
    --page-bg: #eeeeec;
    --card-bg: #f4f3f2;
    --ink: #111111;
    --ink-soft: #2a2a2a;
    --rule: #8a8a8a;
    --band: #0c0c0c;
    --band-edge: #bdbdbd;
  }
  * { box-sizing: border-box; margin: 0; padding: 0; }
  html, body {
    width: 966px; height: 1200px; overflow: hidden;
    background: var(--page-bg);
  }
  .canvas { position: relative; width: 966px; height: 1200px; }
  .card {
    position: absolute; left: 93px; width: 780px; height: 450px;
    background: var(--card-bg);
    box-shadow: 0 2px 10px rgba(0,0,0,0.08);
    overflow: hidden;
  }
  .card--front { top: 120px; }
  .card--back { top: 640px; }

  .brand {
    font-family: "Libre Baskerville", Georgia, serif;
    font-weight: 400; color: var(--ink);
    letter-spacing: -0.5px; white-space: nowrap; line-height: 1;
  }
  .card--front .brand { position: absolute; right: 32px; top: 62px; font-size: 54px; }
  .card--back .brand { position: absolute; left: 0; right: 0; top: 160px; text-align: center; font-size: 60px; }

  .contact { font-family: "Open Sans", Arial, sans-serif; color: var(--ink-soft); }
  .holder-name {
    position: absolute; left: 38px; top: 286px;
    font-size: 22px; font-weight: 700; color: var(--ink); line-height: 28px;
  }
  .divider {
    position: absolute; left: 38px; right: 32px; top: 332px;
    height: 1px; background: var(--rule);
  }
  .contact-list { position: absolute; left: 38px; top: 342px; list-style: none; }
  .contact-list li {
    display: flex; align-items: center; gap: 12px;
    font-size: 18px; line-height: 26px;
  }
  .contact-list svg { width: 14px; height: 16px; flex: none; }
  .company-meta {
    position: absolute; right: 32px; top: 346px;
    text-align: right; font-size: 18px; line-height: 26px; letter-spacing: 0.6px;
  }
  .band-edge {
    position: absolute; left: 0; right: 0; bottom: 30px;
    height: 4px; background: var(--band-edge);
  }
  .band {
    position: absolute; left: 0; right: 0; bottom: 12px;
    height: 18px; background: var(--band);
  }
  .web-spaced {
    position: absolute; left: 0; right: 0; top: 380px;
    text-align: center; font-size: 17px; letter-spacing: 7px; color: var(--ink);
  }
</style>
</head>
<body>
<main class="canvas">
  <section class="card card--front" aria-label="Business card front">
    <div class="brand">LumaVek</div>
    <div class="contact holder-name">Dax Pell</div>
    <div class="divider"></div>
    <ul class="contact contact-list">
      <li>
        <svg viewBox="0 0 14 16" aria-hidden="true"><rect x="2" y="0.5" width="10" height="15" rx="1.5" fill="none" stroke="#222" stroke-width="1.6"/><rect x="4" y="2.5" width="6" height="9" fill="#222"/></svg>
        +65 84126079
      </li>
      <li>
        <svg viewBox="0 0 14 16" aria-hidden="true"><rect x="0.5" y="4" width="13" height="9" fill="#222"/><path d="M0.5 4 L7 9 L13.5 4" fill="none" stroke="#f4f3f2" stroke-width="1.2"/></svg>
        tan@lumavek.example
      </li>
    </ul>
    <div class="contact company-meta">
      <div>www.lumavek.example</div>
      <div>Reg No: 20481957K</div>
    </div>
    <div class="band-edge"></div>
    <div class="band"></div>
  </section>

  <section class="card card--back" aria-label="Business card back">
    <div class="brand">LumaVek</div>
    <div class="contact web-spaced">www.lumavek.example</div>
  </section>
</main>
</body>
</html>
```